KOVER Wealth Partners Brochure
Brochure Design 2011
Your Objectives Through Independence
We need a tri-fold brochure for our company KOVER Wealth Partners. We already have a custom logo created and need that inserted into the brochure. We are a independent financial services company, we offer investment advice and products to consumers and business.
Financial Services
Consumers & Business
Must use our current company logo,you can get it here:
https://photoshelf-example.net/MarcusLindt/KOVERWealthPartners?authkey=Xq7TmLbNZr2Wd9YkHfPe&feat=directlink
Also need all content including sections to be editable. Need at least three sections (Example: "The Company", "Our Services", etc...)
KOVER Wealth Partners Logo
Logo AI file
Logo AI File 2.0
Old Brochure Cover (Prime Ledger)
old brochure Inner (Prime Ledger)
This is a brochure which I like the style, simple and clean
Another Brochure in which I like
by far my favorite one, hope this inspires some ideas
more ideas

```html
<!DOCTYPE html>
<html lang="en">
<head>
<meta charset="utf-8">
<title>KOVER Wealth Partners Brochure</title>
<link href="https://fonts.googleapis.com/css2?family=Roboto+Condensed:ital,wght@0,400;0,700;1,400;1,700&family=Open+Sans:ital,wght@0,400;0,600;1,400;1,700&display=swap" rel="stylesheet">
<style>
  :root {
    --paper: #ffffff;
    --backdrop: #ececec;
    --ink: #5f6062;
    --ink-dark: #3e3f41;
    --lime: #c5d12a;
    --lime-deep: #a9b61c;
    --tab-trust: #4a4b4d;
    --tab-estate: #e0137a;
    --tab-tax: #7fb21f;
    --tab-planning: #1ca6de;
    --tab-mortgage: #f39a1e;
    --photo-blue: #7fb2d6;
    --photo-blue-light: #d7e8f3;
    --photo-skin: #9b7a66;
    --photo-dark: #2d3036;
  }
  * { margin: 0; padding: 0; box-sizing: border-box; }
  html, body { width: 1200px; height: 847px; overflow: hidden; background: var(--backdrop); }
  .brochure {
    position: relative; width: 1200px; height: 847px;
    background: var(--paper); overflow: hidden;
    font-family: "Open Sans", Arial, sans-serif;
  }
  .service-tabs {
    position: absolute; top: 0; left: 300px; display: flex; gap: 38px;
  }
  .service-tab {
    width: 118px; padding-top: 6px;
    font-family: "Roboto Condensed", Arial, sans-serif;
    color: var(--ink); font-size: 14px; line-height: 1.05;
  }
  .service-tab .tab-bar {
    display: block; height: 26px; color: #fff;
    font-weight: 700; font-size: 20px; padding: 2px 8px; text-transform: lowercase;
  }
  .service-tab .tab-sub { display: block; padding: 3px 8px; }
  .tab-trust .tab-bar { background: var(--tab-trust); }
  .tab-estate .tab-bar { background: var(--tab-estate); }
  .tab-tax .tab-bar { background: var(--tab-tax); }
  .tab-planning .tab-bar { background: var(--tab-planning); }
  .tab-mortgage .tab-bar { background: var(--tab-mortgage); }

  .photo-currency {
    position: absolute; left: 0; top: 90px; width: 360px; height: 190px;
    background: radial-gradient(ellipse at 45% 50%, var(--photo-blue) 0%, var(--photo-blue-light) 55%, var(--paper) 85%);
  }
  .photo-workstation {
    position: absolute; left: 0; top: 280px; width: 380px; height: 300px;
    background: linear-gradient(110deg, var(--photo-skin) 0%, var(--photo-dark) 45%, #8a8d94 80%, var(--paper) 100%);
  }

  .headline {
    position: absolute; left: 395px; top: 195px; width: 480px;
    text-align: right;
    font-family: "Roboto Condensed", Arial, sans-serif; font-weight: 700;
    text-transform: uppercase; line-height: 0.95;
  }
  .headline .line-lead { color: var(--lime-deep); font-size: 44px; display: block; }
  .headline .line-mid { color: var(--ink); font-size: 62px; display: block; }
  .headline .line-key { color: var(--ink); font-size: 72px; display: block; letter-spacing: -1px; }
  .headline-rule {
    position: absolute; left: 380px; top: 385px; width: 500px; height: 5px; background: var(--lime);
  }
  .brand {
    position: absolute; left: 905px; top: 290px; display: flex; align-items: center; gap: 10px;
    font-family: "Roboto Condensed", Arial, sans-serif; font-weight: 700;
    color: var(--ink-dark); font-size: 22px; letter-spacing: 0.3px; white-space: nowrap;
  }
  .brand-square { width: 20px; height: 20px; background: var(--lime); flex: none; }
  .web-address {
    position: absolute; left: 935px; top: 340px;
    font-size: 15px; color: var(--ink);
  }

  .quote-band {
    position: absolute; left: 0; top: 580px; width: 1200px; height: 267px;
    background: var(--lime);
    display: flex; align-items: center; justify-content: center;
  }
  .testimonial {
    width: 900px; text-align: center; font-style: italic;
    color: var(--ink-dark); font-size: 30px; line-height: 1.35;
  }
  .testimonial strong { font-weight: 700; font-size: 36px; }
  .testimonial .mark {
    font-family: Georgia, serif; font-style: normal; font-weight: 700;
    font-size: 64px; line-height: 0; vertical-align: -18px; color: var(--ink-dark);
  }
</style>
</head>
<body>
<div class="brochure">
  <nav class="service-tabs">
    <div class="service-tab tab-trust"><span class="tab-bar">trust</span><span class="tab-sub">services</span></div>
    <div class="service-tab tab-estate"><span class="tab-bar">real estate</span><span class="tab-sub">services</span></div>
    <div class="service-tab tab-tax"><span class="tab-bar">tax</span><span class="tab-sub">services</span></div>
    <div class="service-tab tab-planning"><span class="tab-bar">financial</span><span class="tab-sub">planning</span></div>
    <div class="service-tab tab-mortgage"><span class="tab-bar">mortgage</span><span class="tab-sub">lending</span></div>
  </nav>

  <div class="photo-currency" role="img" aria-label="Rendered blue dollar signs"></div>
  <div class="photo-workstation" role="img" aria-label="Hand typing on a laptop keyboard"></div>

  <h1 class="headline">
    <span class="line-lead">Your Objectives</span>
    <span class="line-mid">Through</span>
    <span class="line-key">Independence</span>
  </h1>
  <div class="headline-rule"></div>

  <div class="brand"><span class="brand-square"></span>KOVER Wealth Partners</div>
  <div class="web-address">www.koverwp.com</div>

  <section class="quote-band">
    <p class="testimonial">
      <span class="mark">&ldquo;</span> KOVER&rsquo;s single source, financial services business model is <strong>brilliant</strong> in its simplicity and execution. <span class="mark">&rdquo;</span>
    </p>
  </section>
</div>
</body>
</html>
```